Stationery Design Project

I have recently had developed a logo for my new company Northbay Venture Partners -see logo attached.
I now need the following
1. Letterhead design as Word template
text needs to show the logo and then
Northbay Venture Partners Pty Ltd
ABN 83 402 615 938
Level 5, Arbour House
17 Pellmont Place
Carrow Heights, NSW 2784
Tel: + 61(0)2 9374 2816
www.northbayventurepartners.com
lucasd@northbayventurepartners.com
2. Business card -print ready -
Front side needs to show logo then text as follows
Lucas Drayton
CEO
Level 5, Arbour House
17 Pellmont Place
Carrow Heights, NSW 2784
T: + 61 (0)2 9374 2816
M: + 61 (0)438 721 604
lucasd@pelvarogroup.com.au
On the back of the business card should appear the logo then text as follows
Correct text for the back of the card now in the attached word file please use bold and italics as indicated. Thanks
3. With compliments slip: Including logo + the web address www.northbayventurepartners.com
With compliments slip should fit 3 to an A4 sheet
4. Envelop design including logo + address
For the ethos of the company original brief for the logo below:
I am creating a new business advisory company called Northbay Venture Partners. the Web address will be www.northbayventurepartners.com This business is focused on assisting medium size businesses to achieve their growth objectives. The three pillars are self explanatory -it is focused on businesses that seek to build a global footprint, they seek to define/refine their business model and strategy, they are forward looking and focused on achieving growth.
The ethos of this company will be innovative thinking, passionate, dynamic, entrepreneurial this should reflected in the logo. That said the Logo should not be 'complicated' it should be simple and elegant...
Thanks Lucas Drayton
Reason: I have been travelling all this week -so will only get a chance to review this weekend. Thanks
Target Market(s)
Medium sized business owners with sales between US$5m and $50m.
Industry/Entity Type
Business
Look and feel

```html
<!DOCTYPE html>
<html lang="en">
<head>
<meta charset="utf-8">
<title>Northbay Venture Partners – Business Card</title>
<link rel="stylesheet" href="https://fonts.googleapis.com/css2?family=Alegreya+Sans:wght@400;500;700;800&display=swap">
<style>
  :root {
    --stage: #e4e1dc;
    --blue-deep: #1460b8;
    --blue-mid: #1f86d3;
    --blue-light: #35b6e3;
    --white: #ffffff;
    --mark-grey: #dfe6ee;
    --card-white: #fbfbfc;
    --ink-blue: #1b55a8;
    --ink-grey: #5d6570;
  }
  * { box-sizing: border-box; margin: 0; padding: 0; }
  html, body {
    width: 1200px; height: 1023px; overflow: hidden;
    background: var(--stage);
    font-family: "Alegreya Sans", "Trebuchet MS", sans-serif;
  }
  .sheet {
    width: 1200px; height: 1023px;
    display: flex; flex-direction: column; align-items: center; justify-content: center;
    gap: 70px;
  }
  .card {
    width: 700px; height: 400px; border-radius: 6px; position: relative; overflow: hidden;
    box-shadow: 0 10px 28px rgba(0,0,0,.18);
  }

  /* Back of card */
  .card-back {
    background: radial-gradient(ellipse at 35% 70%, var(--blue-light) 0%, var(--blue-mid) 45%, var(--blue-deep) 100%);
    color: var(--white);
  }
  .card-back .brand-mark {
    position: absolute; right: 34px; top: 40px; bottom: 40px; width: 190px;
    display: flex; flex-direction: column; align-items: center; justify-content: center; gap: 18px;
    color: var(--mark-grey); text-align: center;
  }
  .brand-mark .dot {
    width: 74px; height: 74px; border-radius: 50%; background: var(--mark-grey);
  }
  .brand-mark .name {
    font-weight: 800; font-size: 30px; line-height: 1.05;
  }
  .card-back .pitch {
    position: absolute; left: 46px; top: 48px; width: 430px;
  }
  .pitch h2 {
    font-weight: 700; font-size: 30px; line-height: 1.15; margin-bottom: 22px;
  }
  .services { list-style: none; font-size: 17px; line-height: 1.55; }
  .services li { display: flex; align-items: center; gap: 10px; white-space: nowrap; }
  .services li::before {
    content: ""; width: 9px; height: 9px; border-radius: 50%;
    border: 2px solid var(--white); flex: none;
  }
  .pitch .web {
    margin-top: 22px; font-weight: 700; font-size: 19px;
  }

  /* Front of card */
  .card-front { background: var(--card-white); color: var(--ink-grey); }
  .card-front .brand-mark {
    position: absolute; left: 46px; top: 50px;
    display: flex; align-items: center; gap: 14px;
    color: var(--ink-blue);
  }
  .card-front .brand-mark .dot { width: 40px; height: 40px; background: var(--ink-blue); }
  .card-front .brand-mark .name { font-size: 24px; font-weight: 800; }
  .contact {
    position: absolute; right: 52px; top: 130px; width: 330px;
    font-size: 17px; line-height: 1.45;
  }
  .contact .person { color: var(--ink-blue); font-weight: 700; font-size: 26px; line-height: 1.1; }
  .contact .role { color: var(--ink-blue); font-size: 17px; margin-bottom: 14px; }
  .contact .lines { margin-top: 10px; }
</style>
</head>
<body>
<main class="sheet">
  <section class="card card-back">
    <div class="pitch">
      <h2>Develop the Right Strategy<br>for your business</h2>
      <ul class="services">
        <li>Be accountable - create your Advisory Board</li>
        <li>Build a Business Plan your team will implement</li>
        <li>Take your business global - Export Market Development</li>
        <li>CEO Groups</li>
        <li>Presentations, Seminars, Conferences</li>
      </ul>
      <p class="web">www.northbayventurepartners.com</p>
    </div>
    <div class="brand-mark">
      <span class="dot"></span>
      <span class="name">Northbay Venture Partners</span>
    </div>
  </section>

  <section class="card card-front">
    <div class="brand-mark">
      <span class="dot"></span>
      <span class="name">Northbay Venture Partners</span>
    </div>
    <div class="contact">
      <p class="person">Lucas Drayton</p>
      <p class="role">CEO</p>
      <p>Level 5, Arbour House<br>17 Pellmont Place<br>Carrow Heights, NSW 2784</p>
      <p class="lines">T: + 61 (0)2 9374 2816<br>M: + 61 (0)438 721 604<br>lucasd@pelvarogroup.com.au<br>www.northbayventurepartners.com</p>
    </div>
  </section>
</main>
</body>
</html>
```